Vantor Scorecard

Redesign KLT's existing Vantor scorecard, which tracks and reports key performance indicators (KPIs) for our clients. The scorecard provides our customers with an at-a-glance view of our on-site performance. Vantor is a tool that automatically populates and reports this data.

Review the attached document and deliver suggested redesign options for the two attached views.
Page 1: Portfolio-wide views (high level rollup of multiple sites)
Page 2: Site-level view
Updates

Project Deadline Extended
Reason: Due to the holiday season within the U.S. around the globe we have decided to extend out deadline in hopes of gaining more participation. We will also be providing comments to the current designs tomorrow.

Font styles to use
Sans Serif

Requirements
Must have
• - Sans serif fonts
- Clean aesthetic
- Utilize the exact key performance indicators as are in the attached mockup
- White background (think Plum-esque)
Nice to have
• - Ideas for animation of design elements
Should not have
• - Pictures (icons are okay)

```html
<!DOCTYPE html>
<html lang="en">
<head>
<meta charset="utf-8">
<title>Vantor Scorecard</title>
<link rel="stylesheet" href="https://fonts.googleapis.com/css2?family=Open+Sans:wght@400;600;700&family=Arimo:wght@400&display=swap">
<style>
  :root {
    --backdrop: #e4e5e6;
    --page: #ffffff;
    --ink: #111111;
    --muted: #444a4e;
    --nav-dark: #2f4552;
    --nav-light: #78b3cc;
    --accent: #5ba8c7;
    --accent-soft: #9fd0e2;
    --brand: #1a1a1a;
    --rule: #7fb6cc;
    --target-line: #555a5e;
    --grid: #c9ced1;
  }
  * { box-sizing: border-box; margin: 0; padding: 0; }
  html, body { width: 943px; height: 1200px; overflow: hidden; }
  body {
    background: var(--backdrop);
    font-family: "Open Sans", Arial, sans-serif;
    color: var(--ink);
    position: relative;
  }
  .page {
    position: absolute;
    left: 145px;
    width: 655px;
    height: 514px;
    background: var(--page);
    box-shadow: 0 1px 3px rgba(0,0,0,0.18);
  }
  .page--portfolio { top: 72px; }
  .page--site { top: 613px; }

  .client-name {
    position: absolute;
    left: 204px; top: 48px;
    display: flex; align-items: center; gap: 8px;
    font-size: 21px; color: var(--brand);
  }
  .client-name .dot {
    width: 20px; height: 20px; border-radius: 50%;
    background: var(--brand);
  }
  .product-name {
    position: absolute;
    right: 40px; top: 54px;
    font-size: 20px; font-weight: 700; color: var(--brand);
  }
  .scope {
    position: absolute;
    right: 41px; top: 84px;
    font-size: 11px; color: var(--muted);
  }
  .heading {
    position: absolute;
    left: 38px; top: 128px;
  }
  .heading h1 {
    font-family: "Arimo", Arial, sans-serif;
    font-weight: 400; font-size: 22px; line-height: 26px;
  }
  .heading .subtitle { font-size: 13px; color: var(--accent); line-height: 17px; }
  .heading .period { font-size: 11px; color: var(--ink); line-height: 19px; }

  .section-nav {
    position: absolute;
    left: 38px; top: 210px;
    width: 121px;
    list-style: none;
  }
  .page--site .section-nav { top: 211px; }
  .section-nav li {
    height: 21px;
    margin-bottom: 3px;
    padding-left: 20px;
    font-size: 10px; line-height: 21px;
    color: #ffffff;
    background: var(--nav-dark);
  }
  .section-nav li.is-light { background: var(--nav-light); }

  .kpi-chart { position: absolute; left: 196px; top: 200px; }
  .kpi-chart text { font-family: "Open Sans", Arial, sans-serif; }

  .score-goal {
    position: absolute;
    left: 427px; top: 434px;
    width: 100px;
    font-size: 11px; color: var(--muted);
  }
  .score-goal::after {
    content: "";
    position: absolute;
    left: 26px; top: 21px;
    width: 72px; height: 1.5px;
    background: var(--accent);
  }
  .score-gauge { position: absolute; left: 536px; top: 394px; }

  .kpi-table {
    position: absolute;
    left: 195px; top: 171px;
    width: 436px;
    border-collapse: collapse;
    font-size: 8px;
    color: var(--muted);
  }
  .kpi-table th {
    background: var(--nav-light);
    color: #ffffff;
    font-weight: 400;
    height: 22px;
    text-align: left;
    padding: 0 9px;
    line-height: 9px;
  }
  .kpi-table th.num { text-align: center; padding: 0 2px; }
  .kpi-table td {
    height: 22.3px;
    padding: 0 9px;
    border-bottom: 1px solid var(--rule);
  }
  .kpi-table td + td { border-left: 1px solid var(--rule); }
  .kpi-table td.num { text-align: center; padding: 0 2px; }
  .kpi-table col.c-kpi { width: 105px; }
  .kpi-table col.c-score { width: 43px; }
  .kpi-table col.c-target { width: 196px; }
  .kpi-table col.c-scored { width: 44px; }
  .kpi-table col.c-possible { width: 48px; }
</style>
</head>
<body>

<section class="page page--portfolio">
  <div class="client-name"><span class="dot"></span>company</div>
  <div class="product-name">KLT Vantor</div>
  <div class="scope">All sites. All Programs&nbsp; July 2013</div>
  <header class="heading">
    <h1>Scorecard</h1>
    <p class="subtitle">KPI Score by Site</p>
    <p class="period">Showing July 2013</p>
  </header>
  <ul class="section-nav">
    <li>Governance</li><li>Cost</li><li>Quality</li><li>EHS</li><li>Personal</li><li>Training</li>
    <li class="is-light">Scorecard/KPIs</li><li class="is-light">Updates</li><li class="is-light">Innovations</li>
  </ul>

  <svg class="kpi-chart" width="430" height="190" viewBox="0 0 430 190">
    <defs>
      <linearGradient id="bar-fill" x1="0" x2="1">
        <stop offset="0" stop-color="#5aa9c8"/><stop offset="0.5" stop-color="#9ed3e6"/><stop offset="1" stop-color="#6cb3cf"/>
      </linearGradient>
    </defs>
    <g font-size="8" fill="#555" text-anchor="end">
      <text x="30" y="12">100%</text><text x="30" y="43">90%</text><text x="30" y="73">80%</text>
      <text x="30" y="104">70%</text><text x="30" y="134">60%</text><text x="30" y="165">50%</text>
    </g>
    <g stroke="var(--grid)" stroke-width="0.7">
      <line x1="35" y1="9" x2="422" y2="9"/><line x1="35" y1="70.2" x2="422" y2="70.2"/>
      <line x1="35" y1="100.8" x2="422" y2="100.8"/><line x1="35" y1="131.4" x2="422" y2="131.4"/>
      <line x1="35" y1="162" x2="422" y2="162"/>
    </g>
    <g fill="url(#bar-fill)">
      <rect x="37.5" y="9" width="8.5" height="153"/><rect x="51.3" y="39.6" width="8.5" height="122.4"/>
      <rect x="65.1" y="48.8" width="8.5" height="113.2"/><rect x="79" y="9" width="8.5" height="153"/>
      <rect x="92.8" y="27.4" width="8.5" height="134.6"/><rect x="106.6" y="39.6" width="8.5" height="122.4"/>
      <rect x="120.4" y="9" width="8.5" height="153"/><rect x="134.2" y="39.6" width="8.5" height="122.4"/>
      <rect x="148.1" y="48.8" width="8.5" height="113.2"/>
      <rect x="161.9" y="9" width="8.5" height="153" fill="#d6ebf3"/>
      <rect x="175.7" y="27.4" width="8.5" height="134.6"/><rect x="189.5" y="39.6" width="8.5" height="122.4"/>
      <rect x="203.3" y="9" width="8.5" height="153"/><rect x="217.2" y="27.4" width="8.5" height="134.6"/>
      <rect x="231" y="39.6" width="8.5" height="122.4"/><rect x="244.8" y="9" width="8.5" height="153"/>
      <rect x="258.6" y="39.6" width="8.5" height="122.4"/><rect x="272.4" y="48.8" width="8.5" height="113.2"/>
      <rect x="286.3" y="9" width="8.5" height="153"/><rect x="300.1" y="27.4" width="8.5" height="134.6"/>
      <rect x="313.9" y="39.6" width="8.5" height="122.4"/><rect x="327.7" y="39.6" width="8.5" height="122.4"/>
      <rect x="341.5" y="9" width="8.5" height="153"/><rect x="355.4" y="39.6" width="8.5" height="122.4"/>
      <rect x="369.2" y="48.8" width="8.5" height="113.2"/><rect x="383" y="9" width="8.5" height="153"/>
      <rect x="396.8" y="27.4" width="8.5" height="134.6"/><rect x="410.6" y="39.6" width="8.5" height="122.4"/>
    </g>
    <line x1="35" y1="39.6" x2="422" y2="39.6" stroke="var(--target-line)" stroke-width="1.6"/>
    <polyline points="166,164 166,178 104,178" fill="none" stroke="#9fb4be" stroke-width="0.7"/>
    <text x="135" y="175" font-size="6" fill="#555" text-anchor="middle">Halden - Fremont</text>
  </svg>

  <p class="score-goal">Site Score Goal 90%</p>
  <svg class="score-gauge" width="90" height="100" viewBox="0 0 90 100" role="img" aria-label="Site score 86 percent">
    <ellipse cx="44" cy="90" rx="26" ry="2.5" fill="#000" opacity="0.12"/>
    <circle cx="44" cy="46" r="33" fill="none" stroke="var(--accent-soft)" stroke-width="8"
            stroke-dasharray="178 30" transform="rotate(-80 44 46)"/>
    <path d="M44 46 m0 -33 a33 33 0 0 1 30 19" fill="none" stroke="var(--accent)" stroke-width="8"/>
    <polygon points="40,4 60,13 40,22" fill="var(--accent)"/>
    <circle cx="44" cy="46" r="24" fill="#111"/>
    <text x="44" y="52" text-anchor="middle" font-family="Open Sans, Arial, sans-serif" font-weight="700" font-size="16" fill="#fff">86%</text>
  </svg>
</section>

<section class="page page--site">
  <div class="client-name"><span class="dot"></span>company</div>
  <div class="product-name">KLT Vantor</div>
  <div class="scope">All sites. All Programs&nbsp; July 2013</div>
  <header class="heading">
    <h1>Scorecard</h1>
    <p class="subtitle">KPI Score by Site</p>
    <p class="period">Showing July 2013</p>
  </header>
  <ul class="section-nav">
    <li>Governance</li><li>Cost</li><li>Quality</li><li>EHS</li><li>Personal</li><li>Training</li>
    <li class="is-light">Scorecard/KPIs</li><li class="is-light">Updates</li><li class="is-light">Innovations</li>
  </ul>

  <table class="kpi-table">
    <colgroup><col class="c-kpi"><col class="c-score"><col class="c-target"><col class="c-scored"><col class="c-possible"></colgroup>
    <thead>
      <tr><th>Key Performance indicator</th><th class="num">KPI Score</th><th>Target</th><th class="num">Scored Points</th><th class="num">Possible Points</th></tr>
    </thead>
    <tbody>
      <tr><td>Complaints</td><td class="num">4</td><td>Less than control limit of 4 commplaints per month</td><td class="num">3</td><td class="num">5</td></tr>
      <tr><td>Quality Audits</td><td class="num">3.2</td><td>3 out of 5 average on all internal and joint audits</td><td class="num">10</td><td class="num">10</td></tr>
      <tr><td>Customer Surveys</td><td class="num">4.7</td><td>4 out of 5 average monthly survey score</td><td class="num">5</td><td class="num">5</td></tr>
      <tr><td>Work Order Completion</td><td class="num">100%</td><td>100% on time monthly completion</td><td class="num">5</td><td class="num">5</td></tr>
      <tr><td>Employees Trained</td><td class="num">100%</td><td>90% or greater</td><td class="num">5</td><td class="num">5</td></tr>
      <tr><td>Recordable Rate</td><td class="num">1.1</td><td>Less than 1.9</td><td class="num">10</td><td class="num">10</td></tr>
      <tr><td>Near Misses</td><td class="num">8</td><td>Less than control limit of 10 naar misses per month</td><td class="num">5</td><td class="num">5</td></tr>
      <tr><td>TOTAL</td><td class="num"></td><td></td><td class="num">42</td><td class="num">45</td></tr>
    </tbody>
  </table>

  <p class="score-goal">Site Score Goal 90%</p>
  <svg class="score-gauge" width="90" height="100" viewBox="0 0 90 100" role="img" aria-label="Site score 86 percent">
    <ellipse cx="44" cy="90" rx="26" ry="2.5" fill="#000" opacity="0.12"/>
    <circle cx="44" cy="46" r="33" fill="none" stroke="var(--accent-soft)" stroke-width="8"
            stroke-dasharray="178 30" transform="rotate(-80 44 46)"/>
    <path d="M44 46 m0 -33 a33 33 0 0 1 30 19" fill="none" stroke="var(--accent)" stroke-width="8"/>
    <polygon points="40,4 60,13 40,22" fill="var(--accent)"/>
    <circle cx="44" cy="46" r="24" fill="#111"/>
    <text x="44" y="52" text-anchor="middle" font-family="Open Sans, Arial, sans-serif" font-weight="700" font-size="16" fill="#fff">86%</text>
  </svg>
</section>

</body>
</html>
```